Corvel Ridge New Website Design

We just changed our logo (thank you PlanHarbor) and company name change from Corvel Ridge Machining to Corvel Ridge Manufacturing. We do CNC Swiss screw machining and multi-axis machines. We make parts for many industries. We make large quantity production parts as well small R&D quantities. You can look at our current (outdated) website: http://www.corvelridgemachining.example to see what we do. We would like a WordPress site, including contact form for "request for quote" . We would also like it to be mobile friendly, and the ability to maintain it ourselves after it is finished I have included our new logo and fonts for references. We would like our site to convey the feeling of precision, capability, and trust worthiness with a very modern look. The new website address is www.corvelridge-mfg.example

Coding

Coded - Design and coding required

Number of Pages Required

5+ page

Font styles to use
Serif
Sans Serif
Other font styles liked:
• fronts included, not sure if they work

Colors

Designer to choose colors to be used in the design.

Requirements
Must have
• Contact Info, request for quote field

```html
<!DOCTYPE html>
<html lang="en">
<head>
<meta charset="utf-8">
<title>Corvel Ridge Manufacturing — Responsive Home Page</title>
<link rel="stylesheet" href="https://fonts.googleapis.com/css2?family=Montserrat:wght@700&family=Roboto:wght@400;500&display=swap">
<style>
  :root {
    --backdrop: #d3e3f4;
    --white: #ffffff;
    --brand-blue: #0f4ea3;
    --brand-navy: #1d3b78;
    --ink: #1b1b1b;
    --body-text: #1f3d7a;
    --hero-dark: #1a0f08;
    --hero-amber: #b5742f;
    --hero-gold: #d9a55e;
    --social-1: #4c6fb9;
    --social-2: #1e7bbf;
    --social-3: #4fb4ea;
  }
  * { box-sizing: border-box; margin: 0; padding: 0; }
  html, body { width: 1200px; height: 632px; overflow: hidden; }
  body {
    background: var(--backdrop);
    font-family: "Roboto", Arial, sans-serif;
    position: relative;
  }

  .screen {
    position: absolute;
    background: var(--white);
    overflow: hidden;
    box-shadow: 0 2px 8px rgba(20, 40, 80, 0.15);
  }
  .screen--desktop { left: 86px; top: 115px; width: 565px; height: 376px; }
  .screen--tablet  { left: 685px; top: 154px; width: 277px; height: 362px; }
  .screen--mobile  { left: 1000px; top: 276px; width: 125px; height: 214px; }

  /* Header */
  .site-header {
    position: absolute; left: 0; top: 0; right: 0;
    background: var(--white);
    display: flex; align-items: center;
    box-shadow: 0 2px 4px rgba(0,0,0,0.25);
    z-index: 2;
  }
  .wordmark {
    display: flex; align-items: center; gap: 4px;
    font-family: "Montserrat", Arial, sans-serif;
    font-weight: 700;
    color: var(--brand-navy);
    white-space: nowrap;
    line-height: 1;
  }
  .wordmark__dot {
    border-radius: 50%;
    background: var(--brand-blue);
    flex: none;
  }
  .main-nav { display: flex; }
  .main-nav a {
    color: var(--ink);
    text-decoration: none;
    font-weight: 500;
    text-transform: uppercase;
    white-space: nowrap;
  }
  .main-nav a.is-active {
    color: var(--brand-blue);
    border-bottom: 1px solid var(--brand-blue);
  }
  .social { display: flex; margin-left: auto; }
  .social span { display: block; border-radius: 3px; }
  .social span:nth-child(1) { background: var(--social-1); }
  .social span:nth-child(2) { background: var(--social-2); }
  .social span:nth-child(3) { background: var(--social-3); }

  /* Hero */
  .hero {
    position: absolute; left: 0; right: 0;
    background:
      radial-gradient(ellipse at 35% 35%, var(--hero-gold) 0%, var(--hero-amber) 30%, rgba(90,50,20,0.9) 60%, var(--hero-dark) 100%);
  }
  .hero__title {
    position: absolute;
    font-family: "Montserrat", Arial, sans-serif;
    font-weight: 700;
    color: var(--white);
    text-transform: uppercase;
    line-height: 1.2;
  }
  .hero__button {
    position: absolute;
    background: var(--brand-blue);
    color: var(--white);
    font-weight: 500;
    text-transform: uppercase;
    border-radius: 999px;
    display: flex; align-items: center; justify-content: center;
    white-space: nowrap;
  }

  /* Desktop */
  .screen--desktop .site-header { height: 51px; padding: 0 24px; }
  .screen--desktop .wordmark { font-size: 12px; }
  .screen--desktop .wordmark__dot { width: 9px; height: 9px; }
  .screen--desktop .main-nav { margin-left: 60px; gap: 14px; }
  .screen--desktop .main-nav a { font-size: 7px; padding-bottom: 2px; }
  .screen--desktop .social { gap: 5px; margin-right: 17px; }
  .screen--desktop .social span { width: 13px; height: 13px; }
  .screen--desktop .hero { top: 51px; height: 325px; }
  .screen--desktop .hero__title { left: 349px; top: 120px; font-size: 21px; }
  .screen--desktop .hero__button { left: 349px; top: 184px; width: 82px; height: 19px; font-size: 6.5px; }

  /* Tablet */
  .screen--tablet .site-header { height: 28px; padding: 0 14px; }
  .screen--tablet .wordmark { font-size: 6.5px; gap: 3px; }
  .screen--tablet .wordmark__dot { width: 5px; height: 5px; }
  .screen--tablet .main-nav { margin-left: 22px; gap: 8px; }
  .screen--tablet .main-nav a { font-size: 4px; padding-bottom: 1px; }
  .screen--tablet .social { gap: 3px; margin-right: 9px; }
  .screen--tablet .social span { width: 7px; height: 7px; border-radius: 2px; }
  .screen--tablet .hero { top: 28px; height: 198px; }
  .screen--tablet .hero__title { left: 174px; top: 70px; font-size: 12.5px; }
  .screen--tablet .hero__button { left: 174px; top: 110px; width: 50px; height: 11px; font-size: 3.8px; }

  .about { position: absolute; left: 0; right: 0; }
  .about__title {
    font-family: "Montserrat", Arial, sans-serif;
    font-weight: 700;
    color: var(--brand-blue);
    text-transform: uppercase;
    line-height: 1;
  }
  .about__text { color: var(--body-text); }

  .screen--tablet .about { top: 258px; left: 12px; width: 135px; }
  .screen--tablet .about__title { font-size: 10px; margin-bottom: 5px; }
  .screen--tablet .about__text { font-size: 5px; line-height: 1.35; margin-bottom: 7px; }

  .parts-grid {
    position: absolute; left: 159px; top: 273px;
    display: grid;
    grid-template-columns: repeat(3, 24px);
    grid-auto-rows: 24px;
    column-gap: 18px; row-gap: 18px;
  }
  .parts-grid span { display: block; border-radius: 50%; }
  .part--steel  { background: radial-gradient(circle, #c9c6bf, #8a877f); }
  .part--copper { background: radial-gradient(circle, #e4a07a, #b3643c); }
  .part--orange { background: radial-gradient(circle, #f29a4a, #c9641e); }
  .part--blue   { background: radial-gradient(circle, #3f7fc4, #1c4d8a); }
  .part--dark   { background: radial-gradient(circle, #8c8a86, #3c3a37); }

  /* Mobile */
  .screen--mobile .site-header { height: 22px; padding: 0 10px 0 12px; }
  .screen--mobile .wordmark { font-size: 5px; gap: 2px; }
  .screen--mobile .wordmark__dot { width: 4px; height: 4px; }
  .menu-toggle { margin-left: auto; display: flex; flex-direction: column; gap: 1.5px; }
  .menu-toggle span { display: block; width: 9px; height: 1px; background: var(--ink); }
  .screen--mobile .hero { top: 22px; height: 118px; }
  .screen--mobile .hero__title { left: 0; right: 0; top: 29px; text-align: center; font-size: 12.5px; }
  .screen--mobile .hero__button { left: 32px; top: 72px; width: 70px; height: 16px; font-size: 5.5px; }
  .screen--mobile .about { top: 162px; left: 10px; right: 8px; }
  .screen--mobile .about__title { font-size: 12.5px; margin-bottom: 4px; }
  .screen--mobile .about__text { font-size: 6.8px; line-height: 1.3; }
</style>
</head>
<body>

  <!-- Desktop view -->
  <section class="screen screen--desktop" aria-label="Desktop home page">
    <header class="site-header">
      <div class="wordmark"><span class="wordmark__dot"></span>Corvel Ridge</div>
      <nav class="main-nav">
        <a class="is-active" href="#">Home</a>
        <a href="#">About Us</a>
        <a href="#">Our Work</a>
        <a href="#">Our Shop</a>
        <a href="#">Get a Quote</a>
      </nav>
      <div class="social" aria-label="Social links"><span></span><span></span><span></span></div>
    </header>
    <div class="hero" role="img" aria-label="Close-up photo of a lathe turning a brass part">
      <h1 class="hero__title">When less<br>is more</h1>
      <a class="hero__button">Learn more</a>
    </div>
  </section>

  <!-- Tablet view -->
  <section class="screen screen--tablet" aria-label="Tablet home page">
    <header class="site-header">
      <div class="wordmark"><span class="wordmark__dot"></span>Corvel Ridge</div>
      <nav class="main-nav">
        <a class="is-active" href="#">Home</a>
        <a href="#">About Us</a>
        <a href="#">Our Work</a>
        <a href="#">Our Shop</a>
        <a href="#">Get a Quote</a>
      </nav>
      <div class="social" aria-label="Social links"><span></span><span></span><span></span></div>
    </header>
    <div class="hero" role="img" aria-label="Close-up photo of a lathe turning a brass part">
      <h1 class="hero__title">When less<br>is more</h1>
      <a class="hero__button">Learn more</a>
    </div>
    <div class="about">
      <h2 class="about__title">About us</h2>
      <p class="about__text">Corvel Ridge Manufacturing is a high quality machining resource providing friendly service, fast turnaround times, and engineering expertise, at competitive pricing.</p>
      <p class="about__text">With 20 years of experience in the industry, Corvel Ridge utilizes certified state of the art equipment partnered with top professionals to maximize the value and quality in your product.</p>
      <p class="about__text">Specializing in precision, Corvel Ridge will provide you with superior products, at affordable prices.</p>
    </div>
    <div class="parts-grid">
      <span class="part--steel" role="img" aria-label="Photo of a machined steel part"></span>
      <span class="part--copper" role="img" aria-label="Photo of a copper disc part"></span>
      <span class="part--orange" role="img" aria-label="Photo of an anodized orange fitting"></span>
      <span class="part--blue" role="img" aria-label="Photo of an anodized blue part"></span>
      <span class="part--steel" role="img" aria-label="Photo of a machined steel part"></span>
      <span class="part--dark" role="img" aria-label="Photo of a dark steel roller"></span>
      <span class="part--copper" role="img" aria-label="Photo of a copper pin"></span>
      <span class="part--steel" role="img" aria-label="Photo of a steel bushing"></span>
      <span class="part--steel" role="img" aria-label="Photo of a steel fitting"></span>
    </div>
  </section>

  <!-- Mobile view -->
  <section class="screen screen--mobile" aria-label="Mobile home page">
    <header class="site-header">
      <div class="wordmark"><span class="wordmark__dot"></span>Corvel Ridge</div>
      <div class="menu-toggle" aria-label="Menu"><span></span><span></span><span></span></div>
    </header>
    <div class="hero" role="img" aria-label="Close-up photo of a lathe turning a brass part">
      <h1 class="hero__title">When less is<br>more</h1>
      <a class="hero__button">Learn more</a>
    </div>
    <div class="about">
      <h2 class="about__title">About us</h2>
      <p class="about__text">Corvel Ridge Manufacturing is a high quality machining resource providing friendly service, fast turnaround times.</p>
    </div>
  </section>

</body>
</html>
```